Home Care App Design

We would like a responsive app design (mobile/web) for an app that will be used by our staff. These need to work display nearly the same for iPhone and Android. The app tracks caregiver tasks (check-in time, daily client activities, caregiver notes, and check out time) and provides updates to team and family members
Updates

I have added individual or grouped pages with better resolution. please let me know if you have any questions

we did not get enough entries so we increase the budget and have not received any new designer entries

Target Market(s)

professional caregivers and family members

Industry/Entity Type

Home Health Care

Font styles to use
Serif

Requirements
Must have
• We currently have a logo - please use colors or slight variants
• We also will need pop-up designs for informational messages and call to actions (with 1-3 options)
Nice to have
• I have attached a sketch of the app, please use this as a guideline. We are looking for ease of use.
• Please feel free to add design aspects that will make it easy to navigate, select options, or enter notes/messages

```html
<!DOCTYPE html>
<html lang="en">
<head>
<meta charset="utf-8">
<title>Kind Hands – Caregiver App Screens</title>
<link href="https://fonts.googleapis.com/css2?family=Inter:wght@400;500;600;700&display=swap" rel="stylesheet">
<style>
  :root{
    --page:#edf4fe;
    --white:#ffffff;
    --ink:#2f3440;
    --muted:#6b7280;
    --soft:#9aa3b2;
    --line:#eef0f4;
    --teal:#3bb9d8;
    --coral:#ec6a6a;
    --mint:#5cc3a0;
    --indigo:#4c5fb8;
    --blue:#3b8ef0;
    --header-top:#6aa7f4;
    --header-bottom:#86b6f6;
    --orange-a:#ff9a3c;
    --orange-b:#ffa94d;
    --star:#f5a623;
    --chart:#3aa826;
    --nav:#c9d3e6;
    --nav-active:#6f8de8;
  }
  *{box-sizing:border-box;margin:0;padding:0}
  html,body{width:1200px;height:870px;overflow:hidden}
  body{background:var(--page);font-family:"Inter",sans-serif;color:var(--ink);position:relative}
  .screen{position:absolute;top:181px;width:234px;height:507px;background:var(--white);overflow:hidden;box-shadow:0 10px 28px rgba(60,90,140,.16)}
  .screen--login{left:181px}
  .screen--messages{left:483px}
  .screen--team{left:784px}
  .status{position:absolute;top:8px;left:0;width:100%;height:14px;font-size:9.5px;font-weight:600;display:flex;justify-content:space-between;padding:0 14px 0 20px;align-items:center;z-index:2}
  .status svg{display:block}

  /* login */
  .login-backdrop{position:absolute;inset:0;background:linear-gradient(170deg,#2ee3ef 0%,#6fc7d4 22%,#5aa9c4 48%,#2f8fc6 72%,#9fb3e2 100%)}
  .brand{position:absolute;top:266px;width:100%;text-align:center;color:var(--white);font-size:21px;font-weight:500;letter-spacing:.3px;display:flex;justify-content:center;align-items:center;gap:6px}
  .brand-dot{width:8px;height:8px;border-radius:50%;background:var(--white)}
  .field{position:absolute;left:37px;width:164px;height:30px;border-radius:15px;background:var(--white);font-size:8px;color:#4a5060;display:flex;align-items:center;padding-left:15px}
  .field--email{top:345px}
  .field--password{top:382px;font-size:12px;letter-spacing:1px;color:#3a4254}
  .login-btn{position:absolute;left:75px;top:424px;width:84px;height:24px;border:1.5px solid var(--white);border-radius:12px;color:var(--white);font-size:6.5px;font-weight:700;display:flex;align-items:center;justify-content:center}

  /* messages */
  .screen-title{position:absolute;top:34px;width:100%;text-align:center;font-size:12px;font-weight:500;color:#4d5361}
  .feed{position:absolute;top:61px;left:11px;right:11px;list-style:none}
  .feed-item{position:relative;height:42.5px;border-bottom:1px solid var(--line);padding-left:37px}
  .feed-icon{position:absolute;left:9px;top:10px;width:24px;height:24px;display:flex;align-items:center;justify-content:center}
  .feed-date{position:absolute;right:15px;top:3px;font-size:5.5px;color:var(--soft)}
  .feed-head{padding-top:10px;font-size:11px;font-weight:600;white-space:nowrap}
  .feed-head small{font-size:7.5px;font-weight:400;color:var(--muted);margin-left:3px}
  .feed-body{font-size:7.5px;color:var(--muted);margin-top:0;white-space:nowrap}
  .t-teal{color:var(--teal)} .t-coral{color:var(--coral)} .t-mint{color:var(--mint)} .t-indigo{color:var(--indigo)}
  .avatar{border-radius:50%;background:radial-gradient(circle at 45% 40%,#b98a6e,#5a3b2c 70%,#2a1d18)}
  .feed-icon .avatar{width:25px;height:25px}
  .fab{position:absolute;left:202px;top:426px;width:20px;height:20px;border-radius:50%;background:var(--blue);display:flex;align-items:center;justify-content:center}
  .tabbar{position:absolute;left:0;right:0;top:458px;bottom:0;border-top:1px solid var(--line);display:flex;justify-content:space-around;align-items:center;padding:0 10px}

  /* team */
  .team-header{position:absolute;top:0;left:0;right:0;height:55px;background:linear-gradient(180deg,var(--header-top),var(--header-bottom))}
  .team-title{position:absolute;top:35px;width:100%;text-align:center;color:var(--white);font-size:12px;font-weight:600}
  .team-search{position:absolute;left:209px;top:38px}
  .sort{position:absolute;top:60px;right:9px;font-size:5px;color:var(--muted);display:flex;align-items:center;gap:3px}
  .sort-select{border:1px solid #c8cdd6;border-radius:5px;padding:1px 5px;width:34px;display:flex;justify-content:space-between;align-items:center}
  .roster{position:absolute;top:74px;left:0;right:0;list-style:none}
  .member{position:relative;height:56.5px;margin:0 10px 0 13px;border-bottom:1px solid var(--line)}
  .member .avatar{position:absolute;left:4px;top:3px;width:44px;height:44px;background:radial-gradient(circle at 45% 40%,#c7a58d,#6b5244 62%,#2e3440)}
  .member-name{position:absolute;left:58px;top:6px;font-size:9.5px;font-weight:600}
  .member:first-child .member-name{font-size:11px;top:4px}
  .member-role{position:absolute;left:58px;top:19px;font-size:7px;color:var(--muted)}
  .member-phone{position:absolute;left:58px;top:32px;font-size:6px;color:var(--muted)}
  .earn-band{position:absolute;top:244px;left:0;right:0;height:31px;background:linear-gradient(90deg,var(--orange-a),var(--orange-b));color:var(--white);font-size:12px;font-weight:600;display:flex;align-items:center;justify-content:center}
  .rating{position:absolute;font-size:8.5px;color:#3d4350;display:flex;align-items:center;gap:3px}
  .rating--team{left:20px;top:290px}
  .rating--you{left:23px;top:306px}
  .bonus{position:absolute;top:283px;width:40px;text-align:center;font-size:6.5px;color:#3d4350;line-height:1.1}
  .bonus svg{display:block;margin:0 auto 1px}
  .bonus-value{position:absolute;top:11px;left:0;width:100%;font-size:6.5px}
  .bonus--score{left:131px}
  .bonus--amount{left:173px}
  .total-label{position:absolute;left:20px;top:334px;font-size:8.5px;color:var(--muted)}
  .total-value{position:absolute;left:20px;top:345px;font-size:16px;font-weight:700;color:#2f3440}
  .chart{position:absolute;left:14px;top:370px;width:206px;height:80px;border:1px solid #dde2ea;border-radius:2px}
</style>
</head>
<body>

<!-- Sign-in -->
<section class="screen screen--login">
  <div class="login-backdrop" role="img" aria-label="Photo of caregivers' hands stacked together, tinted in turquoise and blue"></div>
  <div class="status" style="color:#1d2430">
    <span>9:41</span>
    <svg width="42" height="8" viewBox="0 0 42 8"><rect x="0" y="5" width="2" height="3" fill="#1d2430"/><rect x="3" y="3.5" width="2" height="4.5" fill="#1d2430"/><rect x="6" y="2" width="2" height="6" fill="#1d2430"/><rect x="9" y="0" width="2" height="8" fill="#1d2430"/><path d="M15 3a6 6 0 0 1 8 0M17 5a3 3 0 0 1 4 0" stroke="#1d2430" stroke-width="1.2" fill="none"/><circle cx="19" cy="7" r="0.9" fill="#1d2430"/><rect x="27" y="1" width="13" height="6" rx="1.5" fill="#1d2430"/></svg>
  </div>
  <div class="brand"><span class="brand-dot"></span>kindhands</div>
  <div class="field field--email">mara.lind@mail.com</div>
  <div class="field field--password">•••••••</div>
  <div class="login-btn">LOGIN</div>
</section>

<!-- Messages -->
<section class="screen screen--messages">
  <div class="status">
    <span>9:41</span>
    <svg width="42" height="8" viewBox="0 0 42 8"><rect x="0" y="5" width="2" height="3" fill="#1d2430"/><rect x="3" y="3.5" width="2" height="4.5" fill="#1d2430"/><rect x="6" y="2" width="2" height="6" fill="#1d2430"/><rect x="9" y="0" width="2" height="8" fill="#1d2430"/><path d="M15 3a6 6 0 0 1 8 0M17 5a3 3 0 0 1 4 0" stroke="#1d2430" stroke-width="1.2" fill="none"/><circle cx="19" cy="7" r="0.9" fill="#1d2430"/><rect x="27" y="1" width="13" height="6" rx="1.5" fill="#1d2430"/></svg>
  </div>
  <h1 class="screen-title">Messages</h1>
  <ul class="feed">
    <li class="feed-item">
      <span class="feed-icon"><svg width="18" height="22" viewBox="0 0 18 22"><path d="M9 20C4 14 1.5 11 1.5 8a7.5 7.5 0 0 1 15 0c0 3-2.5 6-7.5 12z" fill="none" stroke="var(--teal)" stroke-width="1.6"/><circle cx="9" cy="6.5" r="2" fill="none" stroke="var(--teal)" stroke-width="1.4"/><path d="M5.5 12a3.5 3.5 0 0 1 7 0" fill="none" stroke="var(--teal)" stroke-width="1.4"/></svg></span>
      <span class="feed-date">4/1/2019</span>
      <p class="feed-head t-teal">Check In <small>@Nora Vale</small></p>
      <p class="feed-body">14 Elm Road, Brookfield MA</p>
    </li>
    <li class="feed-item">
      <span class="feed-icon"><svg width="18" height="22" viewBox="0 0 18 22"><path d="M9 17C5 12 3 10 3 7a6 6 0 0 1 12 0c0 3-2 5-6 10z" fill="none" stroke="var(--coral)" stroke-width="1.6"/><circle cx="9" cy="7" r="2" fill="none" stroke="var(--coral)" stroke-width="1.4"/><line x1="2" y1="21" x2="16" y2="21" stroke="var(--coral)" stroke-width="1.6"/></svg></span>
      <span class="feed-date">5/1/2019</span>
      <p class="feed-head t-coral">Check Out <small>@Nora Vale</small></p>
      <p class="feed-body">14 Elm Road, Brookfield MA</p>
    </li>
    <li class="feed-item">
      <span class="feed-icon"><span class="avatar" role="img" aria-label="Profile photo of Nora Vale"></span></span>
      <span class="feed-date">5/1/2019</span>
      <p class="feed-head t-mint">Message <small>@Nora Vale</small></p>
      <p class="feed-body">Hi! Every thing is fine. All work is done.</p>
    </li>
    <li class="feed-item">
      <span class="feed-icon"><svg width="18" height="22" viewBox="0 0 18 22"><path d="M9 17C5 12 3 10 3 7a6 6 0 0 1 12 0c0 3-2 5-6 10z" fill="none" stroke="var(--coral)" stroke-width="1.6"/><circle cx="9" cy="7" r="2" fill="none" stroke="var(--coral)" stroke-width="1.4"/><line x1="2" y1="21" x2="16" y2="21" stroke="var(--coral)" stroke-width="1.6"/></svg></span>
      <span class="feed-date">5/1/2019</span>
      <p class="feed-head t-coral">Check Out <small>@Tomas</small></p>
      <p class="feed-body">8 Cedar Lane, Westport MA</p>
    </li>
    <li class="feed-item">
      <span class="feed-icon"><svg width="20" height="14" viewBox="0 0 20 14"><g stroke="var(--indigo)" stroke-width="1.5"><line x1="0" y1="1" x2="2" y2="1"/><line x1="4" y1="1" x2="20" y2="1"/><line x1="0" y1="5" x2="2" y2="5"/><line x1="4" y1="5" x2="20" y2="5"/><line x1="0" y1="9" x2="2" y2="9"/><line x1="4" y1="9" x2="20" y2="9"/><line x1="0" y1="13" x2="2" y2="13"/><line x1="4" y1="13" x2="20" y2="13"/></g></svg></span>
      <span class="feed-date">5/1/2019</span>
      <p class="feed-head t-indigo">Remainders <small>@you</small></p>
      <p class="feed-body">New appointment</p>
    </li>
    <li class="feed-item">
      <span class="feed-icon"><svg width="18" height="18" viewBox="0 0 24 24"><path d="M5 2h4l2 5-2.5 1.5a11 11 0 0 0 7 7L17 13l5 2v4a2 2 0 0 1-2 2A18 18 0 0 1 3 4a2 2 0 0 1 2-2z" fill="none" stroke="var(--indigo)" stroke-width="1.6" stroke-linejoin="round"/></svg></span>
      <span class="feed-date">5/1/2019</span>
      <p class="feed-head t-indigo">Call Evan <small>@you</small></p>
      <p class="feed-body">Remainder</p>
    </li>
  </ul>
  <span class="fab"><svg width="10" height="10" viewBox="0 0 10 10"><path d="M5 0v10M0 5h10" stroke="#fff" stroke-width="1.6"/></svg></span>
  <nav class="tabbar">
    <svg width="20" height="20" viewBox="0 0 20 20"><rect x="1" y="2" width="18" height="14" rx="1.5" fill="none" stroke="var(--nav-active)" stroke-width="1.5"/><path d="M6 16l-2 3" stroke="var(--nav-active)" stroke-width="1.5"/><path d="M5 7h10M5 10h10M5 13h7" stroke="var(--nav-active)" stroke-width="1.3"/></svg>
    <svg width="20" height="20" viewBox="0 0 20 20" fill="none" stroke="var(--nav)" stroke-width="1.3"><circle cx="7" cy="6" r="3.5"/><path d="M1 18a6 6 0 0 1 12 0"/><circle cx="13.5" cy="6" r="3"/><path d="M14 11a5 5 0 0 1 5 7"/></svg>
    <svg width="20" height="20" viewBox="0 0 20 20" fill="none" stroke="var(--nav)" stroke-width="1.3"><circle cx="10" cy="4" r="2.5"/><path d="M6 19v-8a4 4 0 0 1 8 0v8M8 19v-5M12 19v-5"/><circle cx="4" cy="7" r="1.8"/><circle cx="16" cy="7" r="1.8"/></svg>
    <svg width="20" height="20" viewBox="0 0 20 20" fill="none" stroke="var(--nav)" stroke-width="1.3"><circle cx="12" cy="8" r="6.5"/><path d="M12 4v4h3"/><rect x="2" y="12" width="6" height="6" rx="1"/></svg>
    <svg width="20" height="20" viewBox="0 0 20 20" fill="none" stroke="var(--nav)" stroke-width="1.3"><circle cx="8" cy="8" r="5.5"/><path d="M12 12l6 6"/><path d="M5 8a3 3 0 0 1 3-3"/></svg>
  </nav>
</section>

<!-- Team & earnings -->
<section class="screen screen--team">
  <div class="team-header"></div>
  <div class="status">
    <span>9:41</span>
    <svg width="42" height="8" viewBox="0 0 42 8"><rect x="0" y="5" width="2" height="3" fill="#1d2430"/><rect x="3" y="3.5" width="2" height="4.5" fill="#1d2430"/><rect x="6" y="2" width="2" height="6" fill="#1d2430"/><rect x="9" y="0" width="2" height="8" fill="#1d2430"/><path d="M15 3a6 6 0 0 1 8 0M17 5a3 3 0 0 1 4 0" stroke="#1d2430" stroke-width="1.2" fill="none"/><circle cx="19" cy="7" r="0.9" fill="#1d2430"/><rect x="27" y="1" width="13" height="6" rx="1.5" fill="#1d2430"/></svg>
  </div>
  <h1 class="team-title">Kind Hands</h1>
  <svg class="team-search" width="10" height="10" viewBox="0 0 10 10" fill="none" stroke="#fff" stroke-width="1.2"><circle cx="4.5" cy="4.5" r="3.5"/><path d="M7 7l2.5 2.5"/></svg>
  <div class="sort">Sort by <span class="sort-select">Name <svg width="4" height="3" viewBox="0 0 4 3"><path d="M0 0h4L2 3z" fill="#333"/></svg></span></div>
  <ul class="roster">
    <li class="member">
      <span class="avatar" role="img" aria-label="Profile photo of Evan Hale"></span>
      <span class="member-name">Evan Hale</span>
      <span class="member-role">Team Leader</span>
      <span class="member-phone">Phone: +1 555 010 2244</span>
    </li>
    <li class="member">
      <span class="avatar" role="img" aria-label="Profile photo of Iris Cole"></span>
      <span class="member-name">Iris Cole</span>
      <span class="member-role">Alternate Caregiver</span>
      <span class="member-phone">Phone: +1 555 010 2244</span>
    </li>
    <li class="member">
      <span class="avatar" role="img" aria-label="Profile photo of Owen Price"></span>
      <span class="member-name">Owen Price</span>
      <span class="member-role">Alternate Caregiver</span>
      <span class="member-phone">Phone: +1 555 010 2244</span>
    </li>
  </ul>
  <div class="earn-band">Review / Earnings</div>
  <div class="rating rating--team">Team Rating:
    <svg width="36" height="10" viewBox="0 0 36 10" fill="none" stroke="var(--star)" stroke-width=".9"><path id="st" d="M5 .6l1.3 2.8 3 .3-2.3 2 .7 3L5 7.1 2.3 8.7l.7-3-2.3-2 3-.3z"/><use href="#st" x="12.5"/><use href="#st" x="25"/></svg>
  </div>
  <div class="rating rating--you">Your Rating:
    <svg width="48" height="10" viewBox="0 0 48 10" fill="none" stroke="var(--star)" stroke-width=".9"><use href="#st"/><use href="#st" x="12.5"/><use href="#st" x="25"/><use href="#st" x="37.5"/></svg>
  </div>
  <div class="bonus bonus--score">
    <svg width="30" height="28" viewBox="0 0 30 28"><path d="M15 1l4 9 9.5.8-7.2 6.3 2.2 9.4L15 21.5l-8.5 5 2.2-9.4L1.5 10.8 11 10z" fill="none" stroke="var(--star)" stroke-width="1.3" stroke-linejoin="round"/></svg>
    <span class="bonus-value">3.2</span>Bonus<br>Score
  </div>
  <div class="bonus bonus--amount">
    <svg width="30" height="28" viewBox="0 0 30 28"><path d="M15 1l4 9 9.5.8-7.2 6.3 2.2 9.4L15 21.5l-8.5 5 2.2-9.4L1.5 10.8 11 10z" fill="none" stroke="var(--star)" stroke-width="1.3" stroke-linejoin="round"/></svg>
    <span class="bonus-value">$98.9</span>Bonus<br>Amount
  </div>
  <p class="total-label">Total Earnings Amount</p>
  <p class="total-value">$ 4,598.9</p>
  <div class="chart">
    <svg width="206" height="80" viewBox="0 0 206 80" font-family="Inter, sans-serif" font-size="5.5" fill="#6b7280">
      <text x="103" y="10" text-anchor="middle" font-size="6.5">Earnings by month</text>
      <text x="15" y="17" text-anchor="end">4K</text>
      <text x="15" y="30" text-anchor="end">3K</text>
      <text x="15" y="44" text-anchor="end">2K</text>
      <text x="15" y="58" text-anchor="end">1K</text>
      <path d="M20 7V68H196" fill="none" stroke="#c7ccd5" stroke-width=".8"/>
      <path d="M25 58L43 40L62 47L91 34L109 41L133 34C148 32 165 32 190 47" fill="none" stroke="var(--chart)" stroke-width="1.1"/>
      <g text-anchor="middle">
        <text x="31" y="76">Jan</text><text x="54" y="76">Feb</text><text x="77" y="76">Mar</text><text x="101" y="76">Apr</text>
        <text x="124" y="76">May</text><text x="147" y="76">Jun</text><text x="170" y="76">Jul</text><text x="194" y="76">Aug</text>
      </g>
    </svg>
  </div>
  <nav class="tabbar">
    <svg width="20" height="20" viewBox="0 0 20 20"><rect x="1" y="2" width="18" height="14" rx="1.5" fill="none" stroke="var(--nav)" stroke-width="1.5"/><path d="M6 16l-2 3" stroke="var(--nav)" stroke-width="1.5"/><path d="M5 7h10M5 10h10M5 13h7" stroke="var(--nav)" stroke-width="1.3"/></svg>
    <svg width="20" height="20" viewBox="0 0 20 20" fill="none" stroke="var(--nav)" stroke-width="1.3"><circle cx="7" cy="6" r="3.5"/><path d="M1 18a6 6 0 0 1 12 0"/><circle cx="13.5" cy="6" r="3"/><path d="M14 11a5 5 0 0 1 5 7"/></svg>
    <svg width="20" height="20" viewBox="0 0 20 20" fill="none" stroke="var(--nav-active)" stroke-width="1.3"><circle cx="10" cy="4" r="2.5"/><path d="M6 19v-8a4 4 0 0 1 8 0v8M8 19v-5M12 19v-5"/><circle cx="4" cy="7" r="1.8"/><circle cx="16" cy="7" r="1.8"/></svg>
    <svg width="20" height="20" viewBox="0 0 20 20" fill="none" stroke="var(--nav)" stroke-width="1.3"><circle cx="12" cy="8" r="6.5"/><path d="M12 4v4h3"/><rect x="2" y="12" width="6" height="6" rx="1"/></svg>
    <svg width="20" height="20" viewBox="0 0 20 20" fill="none" stroke="var(--nav)" stroke-width="1.3"><circle cx="8" cy="8" r="5.5"/><path d="M12 12l6 6"/><path d="M5 8a3 3 0 0 1 3-3"/></svg>
  </nav>
</section>

</body>
</html>
```